Knockdown rebuild A0 sign.

After a sign done in A0. Provided an example of how we would like it to look.
receive up to $20,000 off your knockdown.
Slogan “building new memories.”
Provided a few house images to be in the background. Only want 1 of the homes but can’t decide on which one.
Remove “sun gate” logo and put slogan in this area.

Target Market(s)

Knockdown rebuild market

Industry/Entity Type

Building

Requirements
Must have
• Similar to sample

```html
<!DOCTYPE html>
<html lang="en">
<head>
<meta charset="utf-8">
<title>Knockdown Rebuild Sign – Building New Memories</title>
<link rel="stylesheet" href="https://fonts.googleapis.com/css2?family=Great+Vibes&family=Poppins:wght@300;400;700;800&display=swap">
<style>
  :root {
    --backdrop: #e8e9eb;
    --ink: #3b3637;
    --paper: #ffffff;
    --charcoal: #2a2828;
    --sky-top: #1f6fc0;
    --sky-mid: #6fa3d8;
    --cloud: #c9d6ea;
    --house-dark: #4a4545;
    --lawn: #6f8f4a;
    --blue-band: #1576c4;
    --blue-deep: #0f6ab8;
    --glow: #e9eef8;
  }
  * { box-sizing: border-box; margin: 0; padding: 0; }
  html, body { width: 1200px; height: 777px; overflow: hidden; }
  body { background: var(--backdrop); position: relative; font-family: "Poppins", sans-serif; }

  .sign {
    position: absolute; top: 114px; width: 391px; height: 552px; overflow: hidden;
  }
  .sign--light { left: 162px; background: var(--paper); }
  .sign--blue  { left: 647px; background: var(--blue-band); }

  .sign__photo {
    position: absolute; left: 0; top: 0; width: 391px; height: 310px;
    background: linear-gradient(180deg, var(--sky-top) 0%, var(--sky-mid) 38%, var(--cloud) 52%, var(--house-dark) 68%, #8a8684 100%);
  }
  .sign__shapes { position: absolute; left: 0; top: 0; width: 391px; height: 552px; }

  .slogan--script {
    position: absolute; left: 38px; top: 30px;
    font-family: "Great Vibes", cursive; font-size: 54px; line-height: 50px;
    color: var(--paper); text-shadow: 0 0 2px rgba(0,0,0,.5);
  }
  .slogan--bold {
    position: absolute; left: 35px; top: 69px;
    font-family: "Poppins", sans-serif; font-weight: 800; font-size: 38px; line-height: 41px;
    color: var(--paper); text-shadow: 1px 2px 0 rgba(0,0,0,.45);
  }
  .slogan__quote {
    position: absolute; left: 35px; top: 22px;
    font-family: "Poppins", sans-serif; font-weight: 800; font-size: 54px; line-height: 54px;
    color: var(--paper); font-style: normal;
  }

  .offer { position: absolute; right: 39px; text-align: right; }
  .offer__lead, .offer__tail { font-weight: 300; white-space: nowrap; }
  .offer__amount { font-weight: 700; white-space: nowrap; }
  .sign--light .offer { top: 346px; color: var(--ink); }
  .sign--light .offer__lead { font-size: 31px; line-height: 40px; }
  .sign--light .offer__amount { font-size: 46px; line-height: 52px; letter-spacing: .5px; }
  .sign--light .offer__tail { font-size: 27px; line-height: 34px; margin-right: 2px; }

  .sign--blue .offer { top: 330px; color: var(--paper); text-shadow: 1px 2px 0 rgba(0,0,0,.35); }
  .sign--blue .offer__lead { font-size: 31px; line-height: 40px; }
  .sign--blue .offer__amount { font-size: 46px; line-height: 52px; letter-spacing: .5px; }
  .sign--blue .offer__tail { font-size: 27px; line-height: 34px; margin-right: 2px; }

  .brand { position: absolute; display: flex; flex-direction: column; align-items: flex-start; }
  .brand__square { width: 35px; height: 35px; background: var(--charcoal); margin-left: 24px; }
  .brand__name { font-size: 6.5px; font-weight: 400; letter-spacing: .6px; margin-top: 4px; white-space: nowrap; }
  .sign--light .brand { left: 29px; top: 486px; }
  .sign--light .brand__name { color: var(--charcoal); }
  .sign--blue .brand { left: 41px; top: 493px; }
  .sign--blue .brand__square { width: 29px; height: 29px; margin-left: 19px; }
  .sign--blue .brand__name { color: var(--charcoal); }

  .terms { position: absolute; top: 520px; font-size: 6.5px; letter-spacing: .2px; white-space: nowrap; }
  .sign--light .terms { right: 39px; color: var(--charcoal); }
  .sign--blue .terms { right: 45px; color: var(--paper); }

  .sign__glow {
    position: absolute; left: -40px; top: 400px; width: 260px; height: 200px;
    background: radial-gradient(ellipse at 50% 50%, var(--glow) 0%, rgba(180,200,235,.6) 30%, rgba(21,118,196,0) 70%);
  }
</style>
</head>
<body>

<section class="sign sign--light" aria-label="Knockdown rebuild sign, white version">
  <div class="sign__photo" role="img" aria-label="Photograph of a modern two-storey home with double garage under a blue cloudy sky"></div>
  <svg class="sign__shapes" viewBox="0 0 391 552" aria-hidden="true">
    <polygon points="226,271 391,250 391,356" fill="var(--charcoal)"/>
    <polygon points="0,302 226,271 391,356 391,552 0,552" fill="var(--paper)"/>
  </svg>
  <h1 class="slogan--script">Building New<br>Memories</h1>
  <div class="offer">
    <p class="offer__lead">RECEIVE UP TO</p>
    <p class="offer__amount">$20,000 OFF</p>
    <p class="offer__tail">YOUR KNOCKDOWN</p>
  </div>
  <div class="brand">
    <span class="brand__square"></span>
    <span class="brand__name">Stonebay Homes</span>
  </div>
  <p class="terms">TERMS AND CONDITIONS APPLY</p>
</section>

<section class="sign sign--blue" aria-label="Knockdown rebuild sign, blue version">
  <div class="sign__photo" role="img" aria-label="Photograph of a modern two-storey home with double garage, lawn and tree under a blue cloudy sky" style="background: linear-gradient(180deg, var(--sky-top) 0%, var(--sky-mid) 38%, var(--cloud) 52%, var(--house-dark) 68%, var(--lawn) 100%);"></div>
  <svg class="sign__shapes" viewBox="0 0 391 552" aria-hidden="true">
    <defs>
      <linearGradient id="bandFade" x1="0" y1="0" x2="1" y2="1">
        <stop offset="0" stop-color="var(--blue-band)"/>
        <stop offset="1" stop-color="var(--blue-deep)"/>
      </linearGradient>
    </defs>
    <polygon points="0,302 223,271 391,306 391,552 0,552" fill="url(#bandFade)"/>
  </svg>
  <div class="sign__glow" aria-hidden="true"></div>
  <span class="slogan__quote" aria-hidden="true">“</span>
  <h1 class="slogan--bold">Building New<br>Memories</h1>
  <div class="offer">
    <p class="offer__lead">RECEIVE UP TO</p>
    <p class="offer__amount">$20,000 OFF</p>
    <p class="offer__tail">YOUR KNOCKDOWN</p>
  </div>
  <div class="brand">
    <span class="brand__square"></span>
    <span class="brand__name">Stonebay Homes</span>
  </div>
  <p class="terms">TERMS AND CONDITIONS APPLY</p>
</section>

</body>
</html>
```